New design of old website

We need a new design of our domain name reseller website.

quilanorte.com

we would also like new design for Logo and all.

the site will be in English and portuguesse,

Industry/Entity Type

Domain

```html
<!DOCTYPE html>
<html lang="en">
<head>
<meta charset="utf-8">
<title>Quilanorte – Domain Reseller</title>
<link href="https://fonts.googleapis.com/css2?family=Ubuntu:wght@400;500;700&display=swap" rel="stylesheet">
<style>
:root{
  --page:#f1f1f1;
  --sky-top:#cddff0;
  --sky-bottom:#e4edf5;
  --brand:#0a64b8;
  --brand-light:#56a8e6;
  --brand-bright:#1a9ee4;
  --ink:#1d3850;
  --outline:#9cc3e6;
  --green:#4cbb00;
  --orange:#ffa800;
  --slate:#444c56;
  --cyan:#00a6e8;
  --white:#ffffff;
}
*{margin:0;padding:0;box-sizing:border-box}
html,body{width:1200px;height:856px;overflow:hidden;background:var(--page)}
body{font-family:"Ubuntu",sans-serif;position:relative;color:var(--ink)}
.stage{position:absolute;inset:0}
.abs{position:absolute}

.lang{left:832px;top:12px;font-size:11px;color:var(--brand);display:flex;gap:12px;align-items:center}
.lang .flag{display:inline-block;width:13px;height:9px;margin-right:5px;vertical-align:-1px}
.flag-en{background:#2a4f9a}
.flag-pt{background:#e8b400;border:2px solid #c8181e}

.logo{left:178px;top:38px;display:flex;align-items:center;gap:8px;font-size:34px;font-weight:700;color:var(--brand-bright);letter-spacing:-0.5px}
.logo .dot{width:30px;height:30px;border-radius:50%;background:var(--brand-bright)}

.login-label{left:651px;top:82px;font-size:11px;color:var(--brand)}
.login-field{left:701px;top:74px;width:226px;height:29px;border:1px solid var(--outline);border-right:none;border-radius:15px 0 0 15px;background:var(--white);font-size:10.5px;color:var(--brand-light);display:flex;align-items:center;padding-left:13px}
.login-field .slash{margin-left:68px;font-size:16px}
.login-field .pass{margin-left:34px;letter-spacing:1px;font-size:12px}
.login-go{left:927px;top:74px;width:29px;height:29px;background:var(--brand);color:var(--white);font-size:11px;display:flex;align-items:center;justify-content:center}
.login-links{left:827px;top:110px;font-size:10.5px;color:var(--brand-light)}

.nav{left:282px;top:146px;display:flex;font-size:12.5px;color:var(--white);font-weight:500}
.nav span{position:absolute;white-space:nowrap}
.search{left:867px;top:138px;width:175px;height:28px;background:var(--white);border-radius:14px 0 0 14px;font-size:11px;color:var(--brand);display:flex;align-items:center;padding-left:48px}
.search svg{position:absolute;right:6px;top:6px}

.hero-text{left:704px;top:237px;width:262px;font-size:15.5px;line-height:21px;color:var(--ink)}
.cta{left:702px;top:396px;width:246px;height:37px;font-size:15.5px;color:var(--white);display:flex;align-items:center;padding-left:27px}

.features{left:177px;top:553px;width:843px;height:130px;display:flex;border-radius:5px;overflow:hidden}
.feature{flex:1;position:relative;color:var(--white)}
.feature-security{background:var(--green)}
.feature-tld{background:var(--orange)}
.feature-automation{background:var(--slate)}
.feature-personal{background:var(--cyan)}
.feature .icon{position:absolute;left:11px;top:10px;width:53px;height:53px;background:var(--white);border-radius:4px;display:flex;align-items:center;justify-content:center}
.feature .icon .art{width:34px;height:34px;border-radius:3px}
.feature h3{position:absolute;left:73px;top:29px;font-size:14.5px;font-weight:400;white-space:nowrap}
.feature p{position:absolute;left:13px;top:73px;font-size:11.5px;line-height:14px;white-space:nowrap}

.footer-links{left:152px;width:849px;top:753px;text-align:center;font-size:11.5px;color:var(--white)}
.footer-links .sep{margin:0 7px}
.copyright{left:152px;width:849px;top:771px;text-align:center;font-size:11px;color:var(--white)}
.social{left:561px;top:794px;display:flex;gap:6px}
.social span{width:21px;height:21px;background:var(--white);border-radius:3px;display:block}
</style>
</head>
<body>
<div class="stage">
<svg class="abs" width="1200" height="856" viewBox="0 0 1200 856">
  <defs>
    <linearGradient id="sky" x1="0" y1="0" x2="0" y2="1">
      <stop offset="0" stop-color="var(--sky-top)"/>
      <stop offset="1" stop-color="var(--sky-bottom)"/>
    </linearGradient>
    <linearGradient id="heroTone" x1="0" y1="0" x2="1" y2="0">
      <stop offset="0" stop-color="#3a3f46"/>
      <stop offset="0.45" stop-color="#8a96a4"/>
      <stop offset="1" stop-color="#4b525c"/>
    </linearGradient>
    <linearGradient id="ctaTone" x1="0" y1="0" x2="0" y2="1">
      <stop offset="0" stop-color="#2aa9ee"/>
      <stop offset="1" stop-color="#0a6ec4"/>
    </linearGradient>
  </defs>
  <rect x="0" y="170" width="1200" height="364" fill="url(#sky)"/>

  <polygon points="822,0 1038,0 1031,35 815,35" fill="none" stroke="var(--outline)"/>
  <polygon points="617,64 986,64 977,127 610,127" fill="none" stroke="var(--outline)"/>

  <polygon points="202,111 1000,111 993,163 189,163" fill="var(--brand-light)"/>
  <polygon points="262,128 1061,128 1050,177 251,177" fill="var(--brand)"/>
  <g stroke="#2f7fcc" stroke-width="1">
    <line x1="335" y1="143" x2="331" y2="163"/>
    <line x1="433" y1="143" x2="429" y2="163"/>
    <line x1="526" y1="143" x2="522" y2="163"/>
    <line x1="608" y1="143" x2="604" y2="163"/>
    <line x1="690" y1="143" x2="686" y2="163"/>
  </g>

  <polygon points="995,407 1028,407 1014,536 980,536" fill="var(--brand-light)"/>
  <polygon points="210,515 1020,515 1014,536 205,536" fill="var(--brand-light)"/>
  <g role="img" aria-label="Photo of a hand holding a laptop with a login screen in front of server racks">
    <polygon points="218,170 1020,170 977,520 178,520" fill="url(#heroTone)"/>
  </g>
  <rect x="999" y="439" width="10" height="10" fill="var(--brand)" transform="skewX(-8)" />
  <rect x="1002" y="458" width="10" height="10" fill="var(--brand)" transform="skewX(-8)" />
  <rect x="1005" y="477" width="10" height="10" fill="var(--brand)" transform="skewX(-8)" />

  <polygon points="694,196 994,196 961,476 660,476" fill="#ffffff" fill-opacity="0.78"/>
  <polygon points="705,396 937,396 948,414 937,433 705,433 702,430 702,399" fill="url(#ctaTone)"/>
  <g fill="none" stroke="#ffffff" stroke-width="3">
    <polyline points="909,404 919,414 909,424"/>
    <polyline points="918,404 928,414 918,424"/>
  </g>

  <polygon points="265,701 1060,701 1055,735 252,735" fill="var(--brand-light)"/>
  <polygon points="171,723 1015,723 1001,834 152,834" fill="var(--brand)"/>
</svg>

<div class="abs lang"><span><i class="flag flag-en"></i>ENGLISH</span><span>/</span><span><i class="flag flag-pt"></i>PORTUGUESSE</span></div>

<div class="abs logo"><span class="dot"></span>QUILANORTE</div>

<div class="abs login-label">LOG IN :</div>
<div class="abs login-field">User name<span class="slash">/</span><span class="pass">●●●●●●</span></div>
<div class="abs login-go">GO</div>
<div class="abs login-links">Register &nbsp;/ Forgot password</div>

<nav class="abs nav">
  <span style="left:0;top:0">HOME</span>
  <span style="left:66px;top:0">WHY QUILANORTE</span>
  <span style="left:183px;top:0">PRODUCTS</span>
  <span style="left:255px;top:0">SERVICES</span>
  <span style="left:337px;top:0">RESELLER</span>
  <span style="left:420px;top:0">CONTACT</span>
</nav>
<div class="abs search">SEARCH
  <svg width="18" height="18" viewBox="0 0 18 18"><circle cx="7" cy="7" r="5.5" fill="none" stroke="var(--brand)" stroke-width="2"/><line x1="11" y1="11" x2="16.5" y2="16.5" stroke="var(--brand)" stroke-width="2.5"/></svg>
</div>

<p class="abs hero-text">The Linwood Makers Circle is designed for the woman who welcomes the opportunities opened by our rapidly changing society to further her own career goals and to help shape the future role of women in our society..</p>
<div class="abs cta">Quick Free Consultation</div>

<section class="abs features">
  <div class="feature feature-security">
    <div class="icon">
      <svg width="36" height="40" viewBox="0 0 36 40"><path d="M18 2 L33 7 V19 C33 29 26 35 18 38 C10 35 3 29 3 19 V7 Z" fill="#2f8a2a"/><path d="M18 6 L29 10 V19 C29 27 24 31 18 34 C12 31 7 27 7 19 V10 Z" fill="#5fcf3a"/><polyline points="11,20 16,25 25,14" fill="none" stroke="#ffffff" stroke-width="3.5"/></svg>
    </div>
    <h3>SECURITY</h3>
    <p>Protecting your brand against against<br>Undesire association.</p>
  </div>
  <div class="feature feature-tld">
    <div class="icon"><div class="art" role="img" aria-label="Chess knight piece illustration" style="background:#1e1e1e"></div></div>
    <h3>TLD EXPECILIST</h3>
    <p>Providing a large portfolio for<br>Your clients.</p>
  </div>
  <div class="feature feature-automation">
    <div class="icon"><div class="art" role="img" aria-label="Note with gears illustration" style="background:#f2d832"></div></div>
    <h3>AUTOMATION</h3>
    <p>Domain process Quick<br>and Reliable.</p>
  </div>
  <div class="feature feature-personal">
    <div class="icon"><div class="art" role="img" aria-label="Person silhouette illustration" style="background:var(--cyan)"></div></div>
    <h3>PERSONAL SERVICE</h3>
    <p>Domain process Quick<br>and Reliable.</p>
  </div>
</section>

<div class="abs footer-links">Home<span class="sep">|</span>About Us<span class="sep">|</span>Membership<span class="sep">|</span>Events<span class="sep">|</span>Gallery<span class="sep">|</span>Market Place<span class="sep">|</span>Contact Us</div>
<div class="abs copyright">© 2013 Linwood Makers Circle</div>
<div class="abs social" aria-label="Social links"><span></span><span></span><span></span></div>
</div>
</body>
</html>
```